Web Design Project

Brightwater Digital owns and operates a large number of editorial websites. These websites provides mostly consumers in the financial services space with information and price comparisons for a particular service.

Brightwater Digital, as the holding company for each of these sites, currently has no website. We need to build a website targeted towards potential partners for our websites. The idea being that when we start a conversation with a partner, they can view our site and obtain some basic information about who we are.

The structure of the site is to be very simple, containing only a brief description about who we are, our contact details and a list of some of our websites:
• CoverQuest.net.au
• AutoPolicyMatcher.com.au
• NestPolicyMatcher.com.au
• WellPolicyMatcher.com.au
• CoverQuestMatcher.com.au
• TripPolicyMatcher.com.au
• CritterPolicyMatcher.com.au
• CashAdvanceMatcher.com.au
• MobileCoolingUnit.com.au
• FixedSaverYields.com.au
• ThriftyHabits.com.au
• PurseGran.com.au
• TameThePlastic.com.au
• PurseMinder.com.au
• ThirdPartyClaimsCoverOzland.com.au
• Trade-Protect.com.au
• AutoPolicyProviders.com.au
• WellPolicyProviders.com.au
• NestPolicyOzland.com
• CoverQuestOzland.com
• WageShieldPolicyOzland.com
• WellPolicyOzland.com
• CritterPolicyOzland.com
• CashAdvancesOzland.com
• PlasticPaysOzland.com
• NestLendersOzland.com
• NestEggFunds.net.au

The design of the site should say 'Internet company', 'professional', 'fresh thinking'. The design should not look like a corporate site that you would see from any corporate services business with images of people in suits. We are ultimately an Internet business and there should be a unique feel to the site.

We are open to a suggestion of a colour pallet as the holding company does not have an established logo.

Some sites that we like are:

http://www.prismwork-studio.co.uk/#home
http://sample00.layoutvault.example/wt_48248/index.html
http://sample00.layoutvault.example/wordpress_46388/
http://mindvolt.example/
http://www.tandora.us/
http://www.kelvorabintu.example/
http://www.slickfrontpages.example/Corporate/design-ideas-detail.html?id=7916
http://trebla.example/
http://orvantek.example/

Reason: Hi all, Apologies, but I need to extend the timeline. One of our key stakeholders is away for the next week. There are a few good designs that we have received to date and there are some tweaks that we would like to see before making a final decision. Thank you to everyone that has submitted designs - Have a great new year. Derek

Reason: Sorry to have to delay the deadline on this, but we did not find anything in the designs really resonated with us. We will have a further think about the existing designs that have been submitted and how we can provide more specific feedback to the designers to make some modifications to the designs.

Target Market(s)

We are targeting insurance companies / brokers that we are talking to. The idea is that we show a professional face to them.

Industry/Entity Type

Financial

Requirements
Must have
• Home Page (possibly integrated with About us details)
Contact Us
Our Sites

```html
<!DOCTYPE html>
<html lang="en">
<head>
<meta charset="utf-8">
<title>Brightwater Digital</title>
<link rel="stylesheet" href="https://fonts.googleapis.com/css2?family=Montserrat:wght@800&family=Open+Sans:ital,wght@0,400;0,600;0,700;1,400&family=PT+Sans+Narrow:wght@400;700&family=PT+Sans:wght@400&display=swap">
<style>
  :root {
    --peach: #fae3c6;
    --page: #ffffff;
    --ink: #4a4a4a;
    --text: #5c5c5c;
    --orange: #f26c0a;
    --orange-dark: #e35f00;
    --orange-light: #ffe0bf;
    --nav-dark: #1e1e1e;
    --hero: #262626;
    --green: #4fa41c;
    --green-light: #7fcc2e;
    --link: #1a1a1a;
    --teal: #2a7fa8;
  }
  * { box-sizing: border-box; margin: 0; padding: 0; }
  html, body { width: 1200px; height: 1059px; overflow: hidden; }
  body {
    position: relative;
    background: var(--peach);
    font-family: "Open Sans", Arial, sans-serif;
    color: var(--text);
  }
  .page {
    position: absolute; left: 189px; top: 0; width: 822px; height: 1059px;
    background: var(--page);
  }
  .abs { position: absolute; }

  /* header */
  .logo {
    left: 216px; top: 20px;
    font-family: "PT Sans Narrow", Arial, sans-serif; font-weight: 400;
    font-size: 38px; color: var(--ink); line-height: 1; white-space: nowrap;
  }
  .main-nav {
    left: 508px; top: 31px; width: 486px; height: 28px;
    background: linear-gradient(#3a3a3a, var(--nav-dark));
    border-radius: 3px;
    clip-path: polygon(0 0, 97.5% 0, 100% 50%, 97.5% 100%, 0 100%);
    display: flex; padding: 0 14px 0 6px; justify-content: space-between;
  }
  .main-nav a {
    flex: none; white-space: nowrap;
    color: #fff; text-decoration: none; font-weight: 700; font-size: 10.8px;
    line-height: 28px; padding: 0 8px; border-right: 1px solid #4a4a4a;
  }
  .main-nav a:last-child { border-right: 0; }

  /* hero */
  .hero {
    left: 189px; top: 82px; width: 822px; height: 319px;
    border-radius: 6px;
    background: radial-gradient(ellipse at 60% 40%, #3a3a3a, var(--hero) 70%);
    overflow: hidden;
  }
  .hero-title {
    left: 58px; top: 68px;
    font-family: "Montserrat", Arial, sans-serif; font-weight: 800;
    font-size: 55px; line-height: 49px; color: #f2f2f2; letter-spacing: 1px;
  }
  .hero-button {
    left: 83px; top: 248px; width: 166px; height: 34px;
    background: linear-gradient(var(--green-light), var(--green));
    color: #fff; font-family: "PT Sans Narrow", Arial, sans-serif; font-weight: 700;
    font-size: 19px; text-align: center; line-height: 34px; border-radius: 2px;
  }
  .hero-monitor {
    left: 388px; top: 55px; width: 265px; height: 245px;
    background: linear-gradient(160deg, #dcdcdc 0%, #f6f6f6 35%, #e94e8c 60%, #c8c8c8 85%, #9a9a9a 100%);
    border-radius: 6px; opacity: .85;
  }
  .hero-mobile {
    left: 663px; top: 135px; width: 135px; height: 170px;
    background: linear-gradient(160deg, #1a1a1a, #4a8fd0 40%, #e0c020 70%, #2a2a2a);
    border-radius: 6px; opacity: .85;
  }
  .hero-caption {
    right: 29px; top: 40px; text-align: right; color: #fff;
    font-family: "PT Sans", Arial, sans-serif; line-height: 1;
  }
  .hero-caption .brand { font-size: 19px; }
  .hero-caption .sub { font-size: 19px; }
  .hero-caption .tag { font-size: 13px; font-style: italic; color: #bbb; }
  .hero-dots { left: 24px; top: 294px; display: flex; gap: 19px; align-items: center; }
  .hero-dots span { width: 11px; height: 11px; border-radius: 50%; background: #555; }
  .hero-dots span.active { width: 16px; height: 16px; background: var(--orange); }
  .arrow { width: 45px; height: 45px; top: 224px; }

  /* headings */
  .section-title {
    font-family: "PT Sans Narrow", Arial, sans-serif; font-weight: 400; font-size: 29px;
    color: var(--ink); line-height: 1; white-space: nowrap;
  }
  .section-title em { font-style: normal; color: var(--orange); }
  .copy { font-size: 10px; line-height: 17.2px; color: var(--text); }

  /* centre panel */
  .centre-panel {
    left: 388px; top: 401px; width: 401px; height: 658px; background: var(--page);
    box-shadow: 0 0 10px rgba(0,0,0,.18);
  }
  .video-frame {
    left: 398px; top: 447px; width: 377px; height: 242px;
    background: #e4e4e4; border: 1px solid #d0d0d0;
  }
  .video-screen { left: 404px; top: 455px; width: 365px; height: 229px; background: #000; }

  .team-photo {
    left: 198px; top: 725px; width: 177px; height: 72px;
    background: linear-gradient(90deg, #c9a48a, #e8e3de 45%, #b98e73 75%, #ddd);
  }

  /* sites list */
  .site-list { left: 799px; top: 460px; width: 172px; list-style: none; }
  .site-list li {
    font-size: 10px; line-height: 22px; border-bottom: 1px solid #e6e6e6;
    padding-left: 8px; position: relative; height: 23px; white-space: nowrap;
  }
  .site-list li::before {
    content: ""; position: absolute; left: 1px; top: 9px;
    border-left: 3px solid #555; border-top: 3px solid transparent; border-bottom: 3px solid transparent;
  }
  .site-list li:last-child { border-bottom: 0; }
  .site-list a { color: var(--link); }

  .contact { left: 799px; top: 748px; width: 205px; font-size: 10px; line-height: 15px; color: #666; }
  .contact p { margin-bottom: 5.5px; }
  .contact b { font-weight: 600; color: #555; }
  .follow-badge {
    left: 799px; top: 848px; width: 54px; height: 44px; border-radius: 4px;
    background: linear-gradient(#8fd3f2, #e9d9a8);
  }
  .follow-text { left: 860px; top: 849px; width: 140px; font-size: 10px; line-height: 15px; color: #555; }
  .follow-text span { color: var(--teal); }

  /* footer */
  .footer-band {
    left: 0; top: 935px; width: 1200px; height: 82px;
    background: linear-gradient(var(--orange), var(--orange-dark));
  }
  .footer-centre {
    left: 388px; top: 930px; width: 401px; height: 84px;
    background: repeating-linear-gradient(135deg, #f58a2c 0 2px, #f07c1a 2px 5px);
    color: #fff; font-family: "PT Sans Narrow", Arial, sans-serif;
    font-size: 40px; text-align: center; line-height: 84px; white-space: nowrap;
  }
  .footer-nav { font-family: "PT Sans Narrow", Arial, sans-serif; font-size: 11px; color: var(--orange-light); white-space: nowrap; }
  .footer-nav span { margin-right: 10px; }
  .footer-nav span::before { content: "› "; }
  .connect {
    left: 799px; top: 964px; font-style: italic; font-size: 14px; color: #fff; white-space: nowrap;
  }
  .social { width: 21px; height: 21px; border-radius: 50%; top: 964px; background: #2e5da8; }
</style>
</head>
<body>
  <div class="page"></div>

  <div class="abs logo">Brightwater Digital</div>
  <nav class="abs main-nav">
    <a href="#">Welcome</a><a href="#">About Us</a><a href="#">Who We Are</a><a href="#">Our Process</a><a href="#">Our Work Team</a><a href="#">Contants</a>
  </nav>

  <section class="abs hero">
    <h1 class="abs hero-title">CREATIVE<br>DESIGN<br>SERVICES</h1>
    <div class="abs hero-button">View Services</div>
    <div class="abs hero-monitor" role="img" aria-label="Desktop monitor showing an ecommerce web interface"></div>
    <div class="abs hero-mobile" role="img" aria-label="Tablet and phone showing the same web interface"></div>
    <div class="abs hero-caption">
      <div class="brand">Brightwater Digital</div>
      <div class="sub">ecommerce</div>
      <div class="tag">web interface</div>
    </div>
    <div class="abs hero-dots"><span class="active"></span><span></span><span></span><span></span></div>
  </section>

  <svg class="abs arrow" style="left:141px" viewBox="0 0 45 45"><circle cx="22.5" cy="22.5" r="22.5" fill="#111"/><path d="M26 12 L16 22.5 L26 33" stroke="#fff" stroke-width="1.6" fill="none"/></svg>
  <svg class="abs arrow" style="left:1016px" viewBox="0 0 45 45"><circle cx="22.5" cy="22.5" r="22.5" fill="#111"/><path d="M19 12 L29 22.5 L19 33" stroke="#fff" stroke-width="1.6" fill="none"/></svg>

  <div class="abs centre-panel"></div>

  <!-- left column -->
  <h2 class="abs section-title" style="left:197px;top:420px">Our <em>Process</em></h2>
  <p class="abs copy" style="left:198px;top:457px;width:178px">Lorem Ipsum is simply dummy text of the printing and typesetting industry. Lorem Ipsum has been the industry's standard dummy text ever since the 1500s, when an unknown printer took a galley of type and scrambled it to make a type specimen book. It has survived not only five centuries, but also the leap into electronic typesetting, remaining essentially unchanged.</p>

  <h2 class="abs section-title" style="left:197px;top:691px">Our <em>Work Team</em></h2>
  <div class="abs team-photo" role="img" aria-label="Team photograph"></div>
  <p class="abs copy" style="left:197px;top:807px;width:190px">Lorem Ipsum is simply dummy text of the printing and typesetting industry. Lorem Ipsum has been the industry's standard dummy text ever since the 1500s,</p>

  <!-- centre column -->
  <h2 class="abs section-title" style="left:398px;top:417px">Featured <em>Video</em></h2>
  <div class="abs video-frame"></div>
  <div class="abs video-screen"></div>
  <svg class="abs" style="left:553px;top:543px" width="62" height="62" viewBox="0 0 62 62">
    <circle cx="31" cy="31" r="29" fill="#2a2a2a" stroke="#8a8a8a" stroke-width="2"/>
    <circle cx="31" cy="31" r="24" fill="#1a1a1a" stroke="#444" stroke-width="1"/>
    <path d="M27 21 L40 31 L27 41 Z" fill="#9ccc1e"/>
  </svg>

  <h2 class="abs section-title" style="left:404px;top:700px">Who <em>We Are</em></h2>
  <div class="abs copy" style="left:405px;top:740px;width:378px;font-size:10.1px">
    <p>Lorem Ipsum is simply dummy text of the printing and typesetting industry. Lorem Ipsum has been the industry's standard dummy text ever since the 1500s, when an unknown printer took a galley of type and scrambled it to make a type specimen book. It has survived not only five centuries, but also the leap into electronic typesetting, remaining essentially unchanged.</p>
    <p style="margin-top:17px">Lorem Ipsum is simply dummy text of the printing and typesetting industry. Lorem Ipsum has been the industry's standard dummy text ever since the 1500s, when an unknown printer took a galley of type and scrambled it to make a type specimen book. It has survived not only five centuries, but also</p>
  </div>

  <!-- right column -->
  <h2 class="abs section-title" style="left:799px;top:420px">Creative <em>Services</em></h2>
  <ul class="abs site-list">
    <li><a href="#">CoverQuest.net.au</a></li>
    <li><a href="#">AutoPolicyMatcher.com.au</a></li>
    <li><a href="#">NestPolicyMatcher.com.au</a></li>
    <li><a href="#">WellPolicyMatcher.com.au</a></li>
    <li><a href="#">CoverQuestMatcher.com.au</a></li>
    <li><a href="#">TripPolicyMatcher.com.au</a></li>
    <li><a href="#">CritterPolicyMatcher.com.au</a></li>
  </ul>

  <h2 class="abs section-title" style="left:798px;top:706px">Quick <em>Contact</em></h2>
  <div class="abs contact">
    <p>Content here, content here', making it look like readable English.</p>
    <p><b>Tel:</b> +123456789</p>
    <p><b>Fax:</b> +123456789</p>
    <p><b>Email:</b> hello@brightwaterdigital.example</p>
  </div>
  <div class="abs follow-badge" role="img" aria-label="Follow us badge illustration"></div>
  <div class="abs follow-text">Vestibulum posu eros vitae nunc<br><span>social.example/brightwater</span></div>

  <!-- footer -->
  <div class="abs footer-band"></div>
  <div class="abs footer-centre">Brightwater Digital</div>
  <div class="abs footer-nav" style="left:204px;top:957px"><span>Welcome</span><span>About Us</span><span>Who We Are</span></div>
  <div class="abs footer-nav" style="left:198px;top:983px"><span>Our Process</span><span>Our Work Team</span><span>Contants</span></div>
  <div class="abs connect">Get Connected with Us!</div>
  <div class="abs social" style="left:949px"></div>
  <div class="abs social" style="left:976px;background:#3aaee0"></div>
</body>
</html>
```